Business card for Sports Apparel business

DOUBLE SIDED DESIGN
We need business cards for a new sports apparel business. We are developing a protective headband for soccer initially.
Corvell is focused on designing and developing head protection products to reduce the likelihood of concussion when playing sports. Exploring and understanding medical insights, material science research, current and former players experiences and governing bodies guidelines has allowed Corvell to develop the safety, style, form and function requirements of a suitable product to bring to market.
Target Market(s)
Mums buying kits for the sons and daughters. Amateur footballers.
Industry/Entity Type
Sporting Good
Contact Information for Business Card
Martin Ashgrove - CEO
Mobile: +44 7391608254
Email: martin@corvell.co.uk
Tel: 0208 5143927
Helena Pardoe - COO
Mob: +44 7356 409183
Email: helena@corvell.co.uk
Tel: 0208 5143927
Duncan Wyvern - CCO
Mob: +44 7468 230517
Email: duncan@corvell.co.uk
Tel: 0208 5143927
Look and feel

```html
<!DOCTYPE html>
<html lang="en">
<head>
<meta charset="utf-8">
<title>Corvell Business Card</title>
<link rel="stylesheet" href="https://fonts.googleapis.com/css2?family=Montserrat:wght@600;700&family=Arimo:wght@400&family=Lato:wght@700&display=swap">
<style>
  :root {
    --stage: #333333;
    --paper: #ffffff;
    --brand-blue: #005a8e;
    --ink: #1a1a1a;
    --logo-grey: #5b5b5b;
  }
  html, body {
    margin: 0;
    padding: 0;
    width: 1200px;
    height: 900px;
    overflow: hidden;
    background: var(--stage);
  }
  .stage {
    position: relative;
    width: 1200px;
    height: 900px;
  }
  .card {
    position: absolute;
    top: 200px;
    width: 310px;
    height: 502px;
    box-shadow: 3px 4px 6px rgba(0,0,0,0.55);
  }
  .card--front {
    left: 253px;
    background: var(--paper);
    border-radius: 62px 0 62px 0;
  }
  .card--back {
    left: 627px;
    width: 309px;
    background: var(--brand-blue);
    border-radius: 0 62px 0 62px;
  }
  .wordmark {
    position: absolute;
    font-family: "Montserrat", sans-serif;
    font-weight: 600;
    letter-spacing: 1px;
    line-height: 1;
    white-space: nowrap;
  }
  .card--front .wordmark {
    left: 50px;
    top: 136px;
    font-size: 38px;
    color: var(--logo-grey);
  }
  .card--back .wordmark {
    left: 0;
    right: 0;
    text-align: center;
    top: 232px;
    font-size: 38px;
    color: var(--paper);
  }
  .person {
    position: absolute;
    left: 33px;
    top: 295px;
  }
  .person__name {
    font-family: "Montserrat", sans-serif;
    font-weight: 700;
    font-size: 19px;
    color: var(--brand-blue);
    margin: 0;
    line-height: 1.1;
    text-transform: uppercase;
  }
  .person__role {
    font-family: "Arimo", sans-serif;
    font-size: 14px;
    color: var(--ink);
    margin: 2px 0 0;
  }
  .contact-list {
    list-style: none;
    margin: 16px 0 0;
    padding: 0;
    font-family: "Arimo", sans-serif;
    font-size: 14px;
    color: var(--ink);
  }
  .contact-list li {
    display: flex;
    align-items: center;
    height: 19px;
  }
  .contact-list svg {
    width: 16px;
    height: 16px;
    margin-right: 6px;
    flex: none;
  }
  .address {
    font-family: "Arimo", sans-serif;
    font-style: normal;
    font-size: 14px;
    line-height: 18px;
    color: var(--ink);
    margin-top: 17px;
  }
  .back-site {
    position: absolute;
    left: 0;
    right: 0;
    top: 441px;
    text-align: center;
    font-family: "Lato", sans-serif;
    font-weight: 700;
    font-size: 13px;
    color: var(--paper);
  }
</style>
</head>
<body>
<main class="stage">
  <section class="card card--front" aria-label="Card front">
    <div class="wordmark">CORVELL</div>
    <div class="person">
      <h1 class="person__name">Martin Ashgrove</h1>
      <p class="person__role">Chief Executive Officer</p>
      <ul class="contact-list">
        <li>
          <svg viewBox="0 0 16 16" aria-hidden="true"><rect x="1" y="1" width="14" height="14" rx="2" fill="none" stroke="#005a8e" stroke-width="1.4"/><path d="M5 4.2c.6-.4 1.1-.2 1.4.4l.5 1c.2.5 0 .9-.4 1.1l-.4.3c.4 1 1.2 1.8 2.2 2.3l.3-.4c.3-.4.7-.5 1.1-.3l1 .5c.6.3.7.9.3 1.4-.6.8-1.5 1.1-2.4.7C6.7 10.4 5.3 9 4.5 7 4.1 6 4.3 5 5 4.2z" fill="#005a8e"/></svg>
          0208 514 3927
        </li>
        <li>
          <svg viewBox="0 0 16 16" aria-hidden="true"><rect x="0.5" y="3" width="15" height="10" fill="#005a8e"/><path d="M1 3.6 8 9l7-5.4M1 12.5l5-4.3M15 12.5l-5-4.3" fill="none" stroke="#fff" stroke-width="1"/></svg>
          martin@corvell.co.uk
        </li>
        <li>
          <svg viewBox="0 0 16 16" aria-hidden="true"><g fill="none" stroke="#005a8e" stroke-width="1.2"><circle cx="8" cy="8" r="7"/><ellipse cx="8" cy="8" rx="3" ry="7"/><path d="M1 8h14M2.2 4.5h11.6M2.2 11.5h11.6"/></g></svg>
          www.corvell.co.uk
        </li>
      </ul>
      <address class="address">27, Kestrel Park Road<br>London, SE14 6QR</address>
    </div>
  </section>

  <section class="card card--back" aria-label="Card back">
    <div class="wordmark">CORVELL</div>
    <div class="back-site">www.corvell.co.uk</div>
  </section>
</main>
</body>
</html>
```